Business Card template designs

We need a lot of Business card designs.
Your designs will get exposure on our newly opened business-card printing website.
We are committed to quality of paper and packages we use, so they will come up very fancy.

Here is your advantage. We will put the profile of the graphic designer on our site so that you can showcase your designs to people around the world and in Japan.

A profile is not mandatory, although we encourage graphic designers to have a profile to get continuous work in the future.
We are looking forward to having many good designs.

The right of the use of design will be owned by us.
The design may be used to the products other than
business cards.

Target Market(s)

designer,photographer,creator,artist

Industry/Entity Type

Printing

Contact Information for Business Card

The back design is important.
Please check the reference file.

Requirements
Must have
• Please include the following, required information on your business card designs.
• Name: Haruka Tanabe
• Title: Designer
• Web: https://www.korimo.co.jp/kr/
• Address: 4-17 Kitaharazono-Cho Nerima-ku, Tokyo
• Email: info@kkorimo.com
• Phone: 03 6184 3970
• Mobile: 070 4213 6087
• * For Japanese sites, we will convert the text portion to Japanese characters.
• * In case of 28mmx70mm only include Name,Enail,Phone and SNS account(https://www.facebook.com/kkorimo.com)
• 1. colorful
• 2. simple
• 3. natural
• 4. modern
• 5. cool
• 6. sporty
• Please make variations of the same image with 3-6
• different colors / patterns for one design so that
• customers can compare and choose.
• If you want to use a same picture, please make make
• copies and paste on each different types of design.
Nice to have
• You may also use, the following non-required information.
• Company Name: Korimo, Inc.
• Fax: 03-6471-2093
• Open space for company logo

```html
<!DOCTYPE html>
<html lang="en">
<head>
<meta charset="utf-8">
<title>Business Card – Haruka Tanabe</title>
<link rel="stylesheet" href="https://fonts.googleapis.com/css2?family=Open+Sans:wght@300;400&display=swap">
<style>
  :root {
    --backdrop: #d9cfc0;
    --card-black: #1d1d1d;
    --text-grey: #8c8c8c;
    --text-light: #d6d6d6;
    --brand-grey: #5c5c5c;
    --brand-silver: #a6a6a6;
  }
  html, body {
    margin: 0;
    padding: 0;
    width: 1200px;
    height: 747px;
    overflow: hidden;
    background: var(--backdrop);
  }
  .canvas {
    position: relative;
    width: 1200px;
    height: 747px;
  }
  .card {
    position: absolute;
    top: 210px;
    width: 540px;
    height: 326px;
    background: var(--card-black);
    border-radius: 3px;
    box-shadow: 0 10px 24px rgba(0,0,0,0.28);
    overflow: hidden;
  }
  .card--front {
    left: 40px;
    background: linear-gradient(135deg, #2a2a2a, #1a1a1a);
  }
  .card--back { left: 620px; }
  .card svg { display: block; }
  .brand-name {
    font-family: "Open Sans", sans-serif;
    font-weight: 400;
    letter-spacing: 5px;
  }
  .brand-name--front {
    font-size: 30px;
    fill: var(--brand-grey);
  }
  .brand-name--back {
    font-size: 17px;
    letter-spacing: 3px;
    fill: var(--brand-silver);
  }
  .holder-name {
    font-family: "Open Sans", sans-serif;
    font-weight: 300;
    font-size: 27px;
    fill: var(--text-grey);
  }
  .holder-title {
    font-family: "Open Sans", sans-serif;
    font-weight: 400;
    font-size: 13px;
    fill: var(--text-grey);
  }
  .contact-line {
    font-family: "Open Sans", sans-serif;
    font-weight: 400;
    font-size: 12.5px;
    fill: var(--text-light);
  }
  .contact-icon { fill: var(--text-light); }
</style>
</head>
<body>
<main class="canvas">

  <section class="card card--front" aria-label="Card front">
    <svg width="540" height="326" viewBox="0 0 540 326">
      <text class="brand-name brand-name--front" x="270" y="174" text-anchor="middle">KORIMO, INC.</text>
    </svg>
  </section>

  <section class="card card--back" aria-label="Card back">
    <svg width="540" height="326" viewBox="0 0 540 326">
      <text class="holder-name" x="232" y="86">Haruka Tanabe</text>
      <text class="holder-title" x="262" y="108">Designer</text>

      <g class="contact-list">
        <g class="contact-item">
          <path class="contact-icon" d="M262 131h12v9h-12z M264 128h8v3h-8z"/>
          <text class="contact-line" x="282" y="140">03 6184 3970</text>
        </g>
        <g class="contact-item">
          <rect x="264" y="152" width="8" height="12" rx="1" fill="none" stroke="var(--text-light)" stroke-width="1.4"/>
          <text class="contact-line" x="282" y="164">070 4213 6087</text>
        </g>
        <g class="contact-item">
          <rect class="contact-icon" x="262" y="178" width="12" height="9"/>
          <path d="M262 178l6 5 6-5" fill="none" stroke="var(--card-black)" stroke-width="1.2"/>
          <text class="contact-line" x="282" y="188">info@kkorimo.com</text>
        </g>
        <g class="contact-item">
          <circle cx="268" cy="207" r="6" fill="none" stroke="var(--text-light)" stroke-width="1.4"/>
          <path d="M262 207h12 M268 201v12" stroke="var(--text-light)" stroke-width="1"/>
          <text class="contact-line" x="282" y="212">https://www.korimo.co.jp/kr/</text>
        </g>
        <g class="contact-item">
          <path class="contact-icon" d="M268 224a5 5 0 0 1 5 5c0 4-5 8-5 8s-5-4-5-8a5 5 0 0 1 5-5z"/>
          <circle cx="268" cy="229" r="1.8" fill="var(--card-black)"/>
          <text class="contact-line" x="282" y="236">4-17 Kitaharazono-Cho Nerima-ku, Tokyo</text>
        </g>
      </g>

      <text class="brand-name brand-name--back" x="120" y="230" text-anchor="middle">KORIMO, INC.</text>
    </svg>
  </section>

</main>
</body>
</html>
```